TIKLOOMTOT WEBSITE DESIGN

We need a website design based on the template- http://varolapixels.com/themes/quartzpage-bootstrap-wordpress-theme/. We purchased template and will build the website using wordpress. It is one page application. We wanted to list all content in one page and make it browser friendly (can be viewed in cell phone, pc, mac, ipad, etc).

The target audience is parents with babies/kids age from 0-5 year old. We wanted to sell the subscription based monthly boxes to the families. The box will include books, toys, crafts, kids consumer products and letter/note/card to the family from the experts. All boxes are customized based on children's age, gender and interests.

We wanted the site main color to be blue.

Please refer to these websites for ideas.
froxi.com
wwws.pebbleharbor.com
http://www.wigglyoats.com/

I've updated the project brief and make the project fund guaranteed. Thanks!

Target Market(s)

Parents with kids age from 0-5 years old. Mainly target to the China market.

Industry/Entity Type

Cell Phone

Colors
3277b5
85abd2
85cae6
33a6d7
0592cd
0355a3
ceddec
cee9f5

Requirements
Must have
• Must provide the design based on the template- http://varolapixels.com/themes/quartzpage-bootstrap-wordpress-theme/.
The site has to be Chinese character friendly since we are going to post Chinese content on the website. No English content.
The registration forms needs to be designed and include in the final deliverable.

```html
<!DOCTYPE html>
<html lang="en">
<head>
<meta charset="utf-8">
<title>TIKLOOMTOT</title>
<link href="https://fonts.googleapis.com/css2?family=Mulish:wght@400;600;700&family=Open+Sans:wght@400;600&display=swap" rel="stylesheet">
<style>
:root{
  --blue-deep:#0355a3;
  --blue-main:#3277b5;
  --blue-mid:#33a6d7;
  --blue-bright:#0592cd;
  --blue-soft:#85cae6;
  --pale:#f5f7f9;
  --ink:#333;
  --text:#555;
  --gold:#f5b700;
}
*{margin:0;padding:0;box-sizing:border-box}
html,body{width:1200px;height:2378px;overflow:hidden;background:#fff}
body{position:relative;font-family:"Open Sans",Arial,sans-serif;color:var(--text)}
.abs{position:absolute}
.display{font-family:"Mulish",Arial,sans-serif}

.topbar{left:0;top:0;width:1200px;height:70px;background:linear-gradient(#3f82c0,#2f6fae)}
.navbar{left:0;top:70px;width:1200px;height:49px;background:#3576b6;border-top:1px solid #5a94cc}
.nav{right:138px;top:82px;display:flex;gap:37px;font-family:"Mulish",sans-serif;font-size:16px;color:#fff;list-style:none}
.brand{left:127px;top:16px;width:160px;height:142px;display:flex;align-items:center;gap:8px}
.brand-dot{width:22px;height:22px;border-radius:50%;background:#fff;flex:none}
.brand-name{font-family:"Mulish",sans-serif;font-weight:700;font-size:20px;color:#fff}

.hero{left:0;top:119px;width:1200px;height:540px;background:linear-gradient(120deg,#e8c9cf 0%,#e9e4e0 35%,#d4cbbf 60%,#b7a59a 80%,#eee9e4 100%)}
.hero-card{left:327px;top:282px;width:546px;height:178px;background:rgba(51,166,215,.82);border:2px solid rgba(255,255,255,.85);border-radius:5px;text-align:center;color:#fff;padding-top:28px}
.hero-card h1{font-family:"Mulish",sans-serif;font-weight:400;font-size:34px;line-height:1.1}
.hero-card h2{font-family:"Mulish",sans-serif;font-weight:400;font-size:24px;margin-top:6px}
.hero-card p{font-size:11px;line-height:17px;margin:10px 36px 0}
.dots{left:562px;top:632px;display:flex;gap:4px}
.dots span{width:12px;height:12px;border-radius:50%;background:#fff}

.about{left:0;top:659px;width:1200px;height:248px;text-align:center}
.section-title{font-family:"Mulish",sans-serif;font-weight:400;font-size:34px}
.about .section-title{color:#222;margin-top:46px}
.about p{font-size:11px;line-height:17px;width:770px;margin:10px auto 0;color:#555}

.experts{left:0;top:907px;width:1200px;height:445px;background:var(--pale);text-align:center}
.experts .section-title{color:var(--blue-deep);margin-top:55px}
.expert{top:120px;width:220px;text-align:center}
.avatar{width:128px;height:128px;border-radius:50%;margin:0 auto;background:linear-gradient(#ddd,#bbb)}
.expert h3{font-family:"Mulish",sans-serif;font-weight:400;font-size:17px;color:var(--blue-deep);margin-top:11px}
.expert p{font-size:10.5px;line-height:17px;margin-top:6px;color:#555}
.btn-info{display:inline-block;margin-top:20px;width:88px;height:30px;line-height:30px;background:var(--blue-deep);color:#fff;font-size:13px}

.order{left:0;top:1352px;width:1200px;height:487px;background:linear-gradient(100deg,#e6e3df 0%,#bfc8d6 30%,#d9dbe0 55%,#c9a58a 80%,#e3dcd3 100%)}
.form{left:797px;top:1398px;width:276px;height:398px;background:var(--blue-bright)}
.form-head{height:46px;background:var(--blue-mid);color:#fff;font-family:"Mulish",sans-serif;font-size:24px;padding:10px 0 0 24px}
.field{margin:10px 0 0 22px;width:234px;height:28px;background:#fff;font-size:11px;color:#555;padding:7px 10px}
.plans{display:flex;gap:11px;margin:8px 0 0 22px}
.plan{width:74px;height:52px;color:#fff;font-size:11px;text-align:center;padding-top:30px;font-weight:600}
.plan.half{background:var(--gold)}
.plan.year{background:var(--blue-deep)}
.submit{margin:14px 0 0 22px;width:234px;height:38px;background:linear-gradient(#1462b8,#033f80);color:#fff;font-size:15px;text-align:center;line-height:38px;font-weight:600;font-family:"Mulish",sans-serif}

.col-title{font-family:"Mulish",sans-serif;font-weight:400;font-size:27px;color:var(--blue-deep)}
.faq{left:127px;top:1904px;width:460px}
.blog{left:626px;top:1904px;width:460px}
.faq h4{font-family:"Mulish",sans-serif;font-weight:400;font-size:17px;color:#333;margin-top:22px}
.blog h4{font-family:"Mulish",sans-serif;font-weight:400;font-size:17px;color:var(--blue-bright);margin-top:20px}
.faq p,.blog p{font-size:11px;line-height:17px;margin-top:6px;color:#555}
.faq h4+p{margin-bottom:14px}

.footer{left:0;top:2263px;width:1200px;height:115px;background:var(--blue-bright);color:#fff}
.foot-nav{left:127px;top:38px;font-family:"Mulish",sans-serif;font-size:16px}
.foot-nav span{margin:0 6px}
.copyright{left:127px;top:74px;font-size:11px}
.social{left:940px;top:30px;display:flex;gap:5px}
.social span{width:30px;height:30px;border-radius:50%;background:#fff}
</style>
</head>
<body>

<div class="abs topbar"></div>
<div class="abs navbar"></div>
<div class="abs brand"><span class="brand-dot"></span><span class="brand-name">TIKLOOMTOT</span></div>
<ul class="abs nav"><li>Order now</li><li>About us</li><li>Our experts</li><li>FAQ</li><li>Share</li><li>CHATLINE</li></ul>

<div class="abs hero" role="img" aria-label="Gift box opened to show a pink teddy bear, a bead-maze toy and a holiday card in tissue paper"></div>
<div class="abs hero-card">
  <h1>Integer congue augue</h1>
  <h2>Morbi porta libero ullamcorper nonummy</h2>
  <p>Curabitur iaculis tempus eros Curabitur vel mi sit amet magna malesuada ultrices Ut nisi erat fermentum vel congue id euismod in elit Fusce ultricies orci ac</p>
</div>
<div class="abs dots"><span></span><span></span><span></span><span></span></div>

<section class="abs about">
  <h2 class="section-title">About Our Company</h2>
  <p>Mauris vel lacus vitae felis vestibulum volutpat Etiam est nunc venenatis in tristique eu imperdiet ac nisl Cum sociis natoque penatibus et magnis dis parturient montes nascetur ridiculus mus In iaculis facilisis massa Etiam eu urna Sed porta Suspendisse quam leo molestie sed luctus quis feugiat in pede Fusce tellus Sed metus augue convallis et vehicula ut</p>
  <p>Mauris vel lacus vitae felis vestibulum volutpat Etiam est nunc venenatis in tristique eu imperdiet ac nisl Cum sociis natoque penatibus et magnis dis parturient montes nascetur ridiculus mus In iaculis facilisis massa Etiam eu urna Sed porta Suspendisse quam</p>
</section>

<section class="abs experts">
  <h2 class="section-title">Our Experts</h2>
  <div class="abs expert" style="left:128px">
    <div class="avatar" role="img" aria-label="Portrait photo of an expert"></div>
    <h3>Dr. Owen R. Calloway</h3>
    <p>Morbi porta libero id ullamcorper nonummy nibh ligula pulvinar metus eget consectetuer augue nisi quis</p>
    <span class="btn-info">More Info</span>
  </div>
  <div class="abs expert" style="left:367px">
    <div class="avatar" role="img" aria-label="Portrait photo of an expert"></div>
    <h3>Linnea Fairbrook</h3>
    <p>Morbi porta libero id ullamcorper nonummy nibh ligula pulvinar metus eget consectetuer augue nisi quis</p>
    <span class="btn-info">More Info</span>
  </div>
  <div class="abs expert" style="left:608px">
    <div class="avatar" role="img" aria-label="Portrait photo of an expert"></div>
    <h3>Dr. Owen R. Calloway</h3>
    <p>Morbi porta libero id ullamcorper nonummy nibh ligula pulvinar metus eget consectetuer augue nisi quis</p>
    <span class="btn-info">More Info</span>
  </div>
  <div class="abs expert" style="left:846px">
    <div class="avatar" role="img" aria-label="Portrait photo of an expert"></div>
    <h3>Dr. Owen R. Calloway</h3>
    <p>Morbi porta libero id ullamcorper nonummy nibh ligula pulvinar metus eget consectetuer augue nisi quis</p>
    <span class="btn-info">More Info</span>
  </div>
</section>

<div class="abs order" role="img" aria-label="Gift box with a light blue teddy bear, toys and craft supplies in tissue paper"></div>
<form class="abs form">
  <div class="form-head">Order Now Form</div>
  <div class="field">Child name</div>
  <div class="field">Gender</div>
  <div class="field">Birth date</div>
  <div class="field">Your email</div>
  <div class="field">Address</div>
  <div class="field">Cell phone</div>
  <div class="plans"><div class="plan half">6 month</div><div class="plan year">1 Year</div></div>
  <div class="submit">ORDER NOW</div>
</form>

<section class="abs faq">
  <h2 class="col-title">FAQ</h2>
  <h4>TIKLOOMTOT?</h4>
  <p>Mauris vel lacus vitae felis vestibulum volutpat Etiam est nunc venenatis in tristique eu imperdiet ac nisl Cum sociis natoque penatibus et ?</p>
  <h4>Vivamus porttitor purus ?</h4>
  <p>Mauris vel lacus vitae felis vestibulum volutpat Etiam est nunc venenatis in tristique eu imperdiet ac nisl Cum sociis natoque penatibus et ?</p>
  <h4>Ut nisi erat fermentum?</h4>
  <p>Mauris vel lacus vitae felis vestibulum volutpat Etiam est nunc venenatis in tristique eu imperdiet ac nisl Cum sociis natoque penatibus et ?</p>
</section>

<section class="abs blog">
  <h2 class="col-title">Recent Blog</h2>
  <h4>Curabitur iaculis tempus eros</h4>
  <p>Mauris vel lacus vitae felis vestibulum volutpat Etiam est nunc venenatis in tristique eu imperdiet ac nisl Cum sociis natoque penatibus et magnis dis parturient montes nascetur ridiculus mus In iaculis facilisis massa</p>
  <h4>Morbi diam mauris viverra in gravida</h4>
  <p>Mauris vel lacus vitae felis vestibulum volutpat Etiam est nunc venenatis in tristique eu imperdiet ac nisl Cum sociis natoque pen</p>
  <h4>Proin nulla arcu nonummy</h4>
  <p>Mauris vel lacus vitae felis vestibulum volutpat Etiam est nunc venenatis</p>
</section>

<footer class="abs footer">
  <div class="abs foot-nav display">Order now<span>|</span>About us<span>|</span>Our experts<span>|</span>FAQ<span>|</span>Share<span>|</span>CHATLINE</div>
  <div class="abs copyright">© 2014 Company Name &nbsp;All right reserved &nbsp;Term of Use</div>
  <div class="abs social"><span></span><span></span><span></span><span></span></div>
</footer>

</body>
</html>
```